The Pipe Lantern business cards

Hi
i have attached a photo, this is how i want the front of my business card to look like:
i want the water drop on the right to be orange
and the water drop on the left to be gloss black
"The" and "Pty Ltd." will be in the same orange as the water drop
and "Pipe Lantern" will be in white
The background of the logo will be a matte black
on the back of the business card i need the following info:
'The Pipe Lantern pty ltd. '
'Plumbing . Drainage . Gas Fitting . Roofing . Jet Blasting . CCTV . '
Also my contact details:
Cal Yardley
0418672913
thepipelantern@mailkestrel.com
Licence# 583016K
Target Market(s)
Strata managers, building managers, the general public
Industry/Entity Type
Business

```html
<!DOCTYPE html>
<html lang="en">
<head>
<meta charset="utf-8">
<title>The Pipe Lantern – Business Cards</title>
<link rel="stylesheet" href="https://fonts.googleapis.com/css2?family=Baloo+2:wght@500;600;700&display=swap">
<style>
  :root {
    --page-bg: #ececec;
    --card-black: #232323;
    --card-black-deep: #151515;
    --band-grey: #6a6a6a;
    --band-grey-light: #7a7a7a;
    --brand-orange: #ee7d1f;
    --text-white: #ffffff;
    --text-soft: #e6e6e6;
  }
  * { box-sizing: border-box; margin: 0; padding: 0; }
  html, body {
    width: 1200px;
    height: 1100px;
    overflow: hidden;
    background: var(--page-bg);
    font-family: "Baloo 2", sans-serif;
  }
  .sheet {
    width: 1200px;
    height: 1100px;
    display: flex;
    align-items: center;
    justify-content: center;
    gap: 30px;
  }
  .card {
    position: relative;
    width: 560px;
    height: 361px;
    background: radial-gradient(ellipse at 50% 45%, var(--card-black) 0%, var(--card-black-deep) 100%);
    box-shadow: 0 6px 18px rgba(0,0,0,0.25);
    overflow: hidden;
  }

  /* Front */
  .card-front .brand {
    position: absolute;
    inset: 0;
    display: flex;
    align-items: center;
    justify-content: center;
    gap: 16px;
    padding: 0 40px;
  }
  .brand-dot {
    width: 52px;
    height: 52px;
    border-radius: 50%;
    background: var(--brand-orange);
    flex: none;
  }
  .brand-name {
    color: var(--text-white);
    font-weight: 700;
    font-size: 32px;
    line-height: 1;
    letter-spacing: 0.3px;
    white-space: nowrap;
  }

  /* Back */
  .card-back .brand {
    position: absolute;
    left: 0; right: 0; top: 52px;
    display: flex;
    align-items: center;
    justify-content: center;
    gap: 10px;
  }
  .card-back .brand-dot { width: 26px; height: 26px; }
  .card-back .brand-name { font-size: 19px; }

  .services-band {
    list-style: none;
    position: absolute;
    left: 0; right: 0;
    top: 150px;
    height: 78px;
    background: linear-gradient(var(--band-grey-light), var(--band-grey));
    display: grid;
    grid-template-columns: repeat(3, auto);
    grid-template-rows: repeat(2, auto);
    grid-auto-flow: column;
    justify-content: center;
    align-content: center;
    column-gap: 52px;
    row-gap: 4px;
  }
  .service {
    display: flex;
    align-items: center;
    gap: 8px;
    color: var(--text-soft);
    font-weight: 500;
    font-size: 19px;
    line-height: 1.2;
  }
  .tick { width: 16px; height: 16px; flex: none; }

  .contact {
    position: absolute;
    left: 0; right: 0;
    top: 276px;
    text-align: center;
    color: var(--text-white);
  }
  .contact-name { font-weight: 600; font-size: 16px; line-height: 1.25; }
  .contact-line { font-weight: 500; font-size: 12px; line-height: 1.45; }
</style>
</head>
<body>
<main class="sheet">

  <section class="card card-front" aria-label="Business card front">
    <div class="brand">
      <span class="brand-dot"></span>
      <span class="brand-name">The Pipe Lantern Pty Ltd.</span>
    </div>
  </section>

  <section class="card card-back" aria-label="Business card back">
    <div class="brand">
      <span class="brand-dot"></span>
      <span class="brand-name">The Pipe Lantern Pty Ltd.</span>
    </div>

    <ul class="services-band">
      <li class="service"><svg class="tick" viewBox="0 0 16 16"><circle cx="8" cy="8" r="8" fill="#ee7d1f"/><path d="M4.3 8.3 L7 10.8 L11.8 5.4" fill="none" stroke="#fff" stroke-width="1.9" stroke-linecap="round" stroke-linejoin="round"/></svg>Plumbing</li>
      <li class="service"><svg class="tick" viewBox="0 0 16 16"><circle cx="8" cy="8" r="8" fill="#ee7d1f"/><path d="M4.3 8.3 L7 10.8 L11.8 5.4" fill="none" stroke="#fff" stroke-width="1.9" stroke-linecap="round" stroke-linejoin="round"/></svg>Drainage</li>
      <li class="service"><svg class="tick" viewBox="0 0 16 16"><circle cx="8" cy="8" r="8" fill="#ee7d1f"/><path d="M4.3 8.3 L7 10.8 L11.8 5.4" fill="none" stroke="#fff" stroke-width="1.9" stroke-linecap="round" stroke-linejoin="round"/></svg>Roofing</li>
      <li class="service"><svg class="tick" viewBox="0 0 16 16"><circle cx="8" cy="8" r="8" fill="#ee7d1f"/><path d="M4.3 8.3 L7 10.8 L11.8 5.4" fill="none" stroke="#fff" stroke-width="1.9" stroke-linecap="round" stroke-linejoin="round"/></svg>Gas Fitting</li>
      <li class="service"><svg class="tick" viewBox="0 0 16 16"><circle cx="8" cy="8" r="8" fill="#ee7d1f"/><path d="M4.3 8.3 L7 10.8 L11.8 5.4" fill="none" stroke="#fff" stroke-width="1.9" stroke-linecap="round" stroke-linejoin="round"/></svg>Jet Blasting</li>
      <li class="service"><svg class="tick" viewBox="0 0 16 16"><circle cx="8" cy="8" r="8" fill="#ee7d1f"/><path d="M4.3 8.3 L7 10.8 L11.8 5.4" fill="none" stroke="#fff" stroke-width="1.9" stroke-linecap="round" stroke-linejoin="round"/></svg>CCTV</li>
    </ul>

    <div class="contact">
      <p class="contact-name">Cal Yardley, 0418672913</p>
      <p class="contact-line">Email: thepipelantern@mailkestrel.com</p>
      <p class="contact-line">Licence# 583016K</p>
    </div>
  </section>

</main>
</body>
</html>
```